SkyvoraQ Business Cards and Stationary Design

Need a design for our business cards and stationary. I want to carry on the theme of the logo. I want the business cards to have a design on the back. I would like the business cards and the stationary to carry the same theme, design scheme, and branding

Target Market(s)

Airlines and Maintenance Facilities

Industry/Entity Type

Aviation

Contact Information for Business Card

Name
Position Title
Address: 4827 Tollbeck Lane, Brennmoor, Calveria, 34951
Office Number
Mobile Number
Email
Website

Font styles to use
Serif
Sans Serif

Colors

Designer to choose colors to be used in the design.

```html
<!DOCTYPE html>
<html lang="en">
<head>
<meta charset="utf-8">
<title>SkyvoraQ Stationery</title>
<link href="https://fonts.googleapis.com/css2?family=Montserrat:wght@700&family=Open+Sans:wght@400;600&display=swap" rel="stylesheet">
<style>
  :root {
    --bg: #d6d7da;
    --blue-light: #2aa3dc;
    --blue-mid: #2470b5;
    --blue-dark: #1b2d68;
    --navy: #14285c;
    --paper: #ffffff;
    --paper-grey: #e7e7ec;
    --ink-soft: #6b7080;
  }
  * { margin: 0; padding: 0; box-sizing: border-box; }
  html, body { width: 1200px; height: 960px; overflow: hidden; }
  body { background: var(--bg); font-family: "Open Sans", Arial, sans-serif; position: relative; }

  .piece { position: absolute; box-shadow: 0 6px 16px rgba(0,0,0,.18); overflow: hidden; }

  .brand-name {
    font-family: "Montserrat", Arial, sans-serif; font-weight: 700;
    color: var(--navy); letter-spacing: .18em; text-transform: uppercase;
    display: flex; align-items: center; gap: 8px; white-space: nowrap;
  }
  .brand-name .dot { width: 14px; height: 14px; border-radius: 50%; background: var(--blue-mid); flex: none; }
  .brand-name.on-blue { color: #fff; }
  .brand-name.on-blue .dot { background: #fff; }

  .blue-grad { background: linear-gradient(100deg, var(--blue-light), var(--blue-mid) 45%, var(--blue-dark)); }
  .silver-grad { background: linear-gradient(160deg, #fff 0%, var(--paper-grey) 100%); }

  /* Folder */
  .folder { left: 40px; top: 40px; width: 340px; height: 470px; display: flex; align-items: flex-end; justify-content: center; padding-bottom: 70px; }
  .folder .brand-name { font-size: 26px; }

  /* Letterhead */
  .letterhead { left: 410px; top: 40px; width: 330px; height: 470px; background: var(--paper); }
  .letterhead .brand-name { position: absolute; top: 26px; right: 24px; font-size: 12px; }
  .letterhead .foot { position: absolute; bottom: 22px; left: 24px; right: 24px; font-size: 8px; color: var(--ink-soft); border-top: 1px solid var(--paper-grey); padding-top: 8px; display: flex; justify-content: space-between; gap: 8px; white-space: nowrap; }

  /* Envelopes */
  .envelope-front { left: 775px; top: 40px; width: 385px; height: 215px; display: flex; align-items: center; padding-left: 40px; }
  .envelope-front .brand-name { font-size: 20px; }
  .envelope-back { left: 775px; top: 295px; width: 385px; height: 215px; }
  .envelope-back .band { position: absolute; left: 0; right: 0; top: 40px; height: 46px; }

  /* Business cards */
  .card { width: 350px; height: 200px; }
  .card-front { left: 40px; top: 560px; }
  .card-front .brand-name { position: absolute; left: 26px; top: 80px; font-size: 14px; }
  .card-front .web { position: absolute; left: 26px; bottom: 18px; font-size: 8px; color: var(--ink-soft); }
  .card-front .panel { position: absolute; right: 0; top: 0; }
  .card-front .details { position: absolute; right: 18px; top: 22px; width: 160px; text-align: right; color: #fff; font-size: 8px; line-height: 1.6; }
  .details .name { font-size: 13px; font-weight: 600; line-height: 1.2; }
  .details .title { font-size: 9px; margin-bottom: 10px; opacity: .9; }
  .details .row { display: flex; justify-content: flex-end; align-items: center; gap: 6px; }
  .details .icon { width: 9px; height: 9px; fill: #fff; flex: none; }

  .card-back { left: 420px; top: 560px; display: flex; align-items: center; justify-content: center; }
  .card-back .brand-name { font-size: 20px; }

  /* Disc sleeve */
  .sleeve { left: 800px; top: 560px; width: 360px; height: 360px; }
  .sleeve .brand-name { position: absolute; left: 40px; bottom: 60px; font-size: 22px; }
  .sleeve .disc-edge { position: absolute; right: -150px; top: 30px; width: 300px; height: 300px; border-radius: 50%; }
</style>
</head>
<body>

  <section class="piece folder blue-grad" aria-label="Presentation folder">
    <div class="brand-name on-blue"><span class="dot"></span>SkyvoraQ</div>
  </section>

  <section class="piece letterhead" aria-label="Letterhead">
    <div class="brand-name"><span class="dot"></span>SkyvoraQ</div>
    <div class="foot"><span>4827 Tollbeck Lane, Brennmoor, Calveria, 34951</span><span>www.skyvoraq.com</span></div>
  </section>

  <section class="piece envelope-front silver-grad" aria-label="Envelope front">
    <div class="brand-name"><span class="dot"></span>SkyvoraQ</div>
  </section>

  <section class="piece envelope-back silver-grad" aria-label="Envelope back">
    <div class="band blue-grad"></div>
  </section>

  <section class="piece card card-front silver-grad" aria-label="Business card front">
    <svg class="panel" width="210" height="200" viewBox="0 0 210 200" aria-hidden="true">
      <defs>
        <linearGradient id="cardPanel" x1="0" y1="0" x2="1" y2="1">
          <stop offset="0" stop-color="#2aa3dc"/>
          <stop offset="1" stop-color="#1b2d68"/>
        </linearGradient>
      </defs>
      <path d="M60 0 H210 V200 H30 C80 150 20 60 60 0 Z" fill="url(#cardPanel)"/>
    </svg>
    <div class="brand-name"><span class="dot"></span>SkyvoraQ</div>
    <div class="web">www.skyvoraq.com</div>
    <div class="details">
      <div class="name">Marcus Lindell</div>
      <div class="title">Chief Executive</div>
      <div class="row"><span>4827 Tollbeck Lane<br>Brennmoor, Calveria, 34951</span>
        <svg class="icon" viewBox="0 0 10 10"><path d="M5 0a3.5 3.5 0 0 0-3.5 3.5C1.5 6 5 10 5 10s3.5-4 3.5-6.5A3.5 3.5 0 0 0 5 0zm0 5a1.5 1.5 0 1 1 0-3 1.5 1.5 0 0 1 0 3z"/></svg></div>
      <div class="row"><span>+1 772 555 0148</span>
        <svg class="icon" viewBox="0 0 10 10"><path d="M2 0l2 2.5-1 1.2a6 6 0 0 0 3.3 3.3l1.2-1L10 8l-1.5 2C4 10 0 6 0 1.5z"/></svg></div>
      <div class="row"><span>info@skyvoraq.com</span>
        <svg class="icon" viewBox="0 0 10 10"><path d="M0 2h10v6H0zM0 2l5 3.5L10 2" stroke="#1b2d68" stroke-width=".8"/></svg></div>
    </div>
  </section>

  <section class="piece card card-back blue-grad" aria-label="Business card back">
    <div class="brand-name on-blue"><span class="dot"></span>SkyvoraQ</div>
  </section>

  <section class="piece sleeve silver-grad" aria-label="Disc sleeve">
    <div class="disc-edge blue-grad"></div>
    <div class="brand-name"><span class="dot"></span>SkyvoraQ</div>
  </section>

</body>
</html>
```